Senior Marketing Postcard

Themed in Red/Navy and Grey. Divide Jumbo postcard into four segments.
First one to include beach/palms/sun with a caption something like "Wish you were there year round?"
Second one to include a pic of an upscale city condo with caption "Ready for one-level living?"
Third one showing Montgomery County, MD tax bill with caption "Time to down-size expenses?"
Fourth with a foot of snow and a snow shoveler with caption "Done with winters?"
- If you answered "YES", then we need to talk!
On back split into two with firm logo, my picture and phone - both cell 301-647-9183 and office 301-836-7100. dora@dorabeckhomes.com and web dorabeckhomes.com
Marketing

```html
<!DOCTYPE html>
<html lang="en">
<head>
<meta charset="utf-8">
<title>Senior Marketing Postcard</title>
<link href="https://fonts.googleapis.com/css2?family=Open+Sans:wght@400;600&family=Questrial&display=swap" rel="stylesheet">
<style>
  :root{
    --red:#d4202a;
    --red-dark:#a5141c;
    --navy:#1f4e96;
    --navy-dark:#163a73;
    --black:#0d0d0f;
    --white:#ffffff;
    --paper:#fbfbfb;
    --rule:#d6d6d6;
    --grey-bg:#d9d4cb;
    --band:#2e2e30;
    --ink:#1c1c1c;
    --page:#eeeeee;
  }
  *{box-sizing:border-box;margin:0;padding:0}
  html,body{width:1200px;height:900px;overflow:hidden;background:var(--page)}
  body{position:relative;font-family:"Open Sans",Arial,sans-serif}

  /* ---------- address side ---------- */
  .card{position:absolute;box-shadow:0 4px 14px rgba(0,0,0,.18)}
  .card--address{left:30px;top:30px;width:660px;height:430px;background:var(--paper)}
  .agent-panel{position:absolute;left:0;top:10px;width:450px;height:380px;background:var(--black);overflow:hidden}
  .agent-panel__red{position:absolute;left:0;top:0;width:100%;height:68px;background:linear-gradient(var(--red),var(--red-dark))}
  .agent-panel__navy{position:absolute;left:0;top:68px;width:100%;height:40px;background:linear-gradient(var(--navy),var(--navy-dark))}
  .firm-mark{position:absolute;left:10px;top:12px;width:172px;height:132px;background:var(--white);border-radius:0 0 10px 0;
    display:flex;flex-direction:column;align-items:center;justify-content:center;gap:6px;color:var(--navy);font-weight:600}
  .firm-mark__square{width:16px;height:16px;background:var(--navy)}
  .firm-mark__name{font-size:19px;line-height:1.1;text-align:center}
  .firm-mark__sub{font-size:13px}
  .agent-photo{position:absolute;left:250px;top:120px;width:190px;height:260px;
    background:linear-gradient(170deg,#3a2b24 0%,#5a4234 45%,#2a2426 100%)}
  .agent-name{position:absolute;left:52px;top:232px;color:var(--white);font-size:20px}
  .contact{position:absolute;left:22px;top:262px;width:215px;height:94px;background:linear-gradient(var(--red),var(--red-dark));border-radius:6px;overflow:hidden}
  .contact__icons{position:absolute;left:0;top:0;width:28px;height:100%;background:var(--navy);display:flex;flex-direction:column;justify-content:space-around;align-items:center;padding:4px 0}
  .contact__icons svg{width:11px;height:11px}
  .contact__list{list-style:none;position:absolute;left:34px;top:4px;color:var(--white);font-size:13.5px;line-height:21.5px;white-space:nowrap}
  .stamp-box{position:absolute;right:26px;top:8px;width:92px;height:96px;border:1px solid var(--rule)}
  .address-line{position:absolute;left:472px;width:176px;height:1px;background:var(--rule)}

  /* ---------- message side ---------- */
  .card--message{left:510px;top:480px;width:660px;height:400px;background:var(--grey-bg)}
  .tile{position:absolute;width:303px;height:150px;border-radius:10px;overflow:hidden;box-shadow:0 2px 6px rgba(0,0,0,.35)}
  .tile--beach{left:20px;top:20px}
  .tile--condo{left:337px;top:20px}
  .tile--tax{left:20px;top:182px}
  .tile--snow{left:337px;top:182px}
  .tile__image{position:absolute;inset:0}
  .tile--beach .tile__image{background:linear-gradient(135deg,#8fc3e6 0%,#c7e2ef 50%,#e4d8bd 100%)}
  .tile--condo .tile__image{background:linear-gradient(135deg,#8a949b 0%,#b9c0c4 55%,#7d868c 100%)}
  .tile--tax .tile__image{background:linear-gradient(135deg,#7a7d80 0%,#d6d6d3 55%,#e6e5e1 100%)}
  .tile--snow .tile__image{background:linear-gradient(135deg,#8d949a 0%,#d3d8dc 55%,#eef1f3 100%)}
  .tile__caption{position:absolute;top:12px;bottom:10px;padding:0 8px;background:rgba(255,255,255,.45);
    font-family:"Questrial",Arial,sans-serif;color:var(--ink);font-size:33px;line-height:1;letter-spacing:-.5px;
    white-space:nowrap;display:flex;flex-direction:column;justify-content:center}
  .tile--beach .tile__caption{left:66px}
  .tile--condo .tile__caption{left:74px;font-size:32px}
  .tile__caption .big{font-size:48px;line-height:1}
  .tile--tax .tile__caption{left:54px;font-size:35px}
  .tile--snow .tile__caption{left:70px;font-size:31px}
  .cta-band{position:absolute;left:0;right:0;bottom:0;height:56px;background:var(--band);color:var(--white);
    font-family:"Questrial",Arial,sans-serif;font-size:24px;display:flex;align-items:center;justify-content:center}
</style>
</head>
<body>

<section class="card card--address" aria-label="Address side">
  <div class="agent-panel">
    <div class="agent-panel__red"></div>
    <div class="agent-panel__navy"></div>
    <div class="firm-mark">
      <span class="firm-mark__square"></span>
      <span class="firm-mark__name">HARTWELL<br>REALTORS</span>
      <span class="firm-mark__sub">A Crestline Co.</span>
    </div>
    <div class="agent-photo" role="img" aria-label="Portrait photo of the agent"></div>
    <p class="agent-name">Dora A. Beck</p>
    <div class="contact">
      <div class="contact__icons">
        <svg viewBox="0 0 12 12"><rect x="3" y="0.5" width="6" height="11" rx="1" fill="none" stroke="#fff"/><rect x="5" y="9" width="2" height="1" fill="#fff"/></svg>
        <svg viewBox="0 0 12 12"><path d="M2 1l2.5 0 1 3-1.5 1a7 7 0 0 0 3 3l1-1.5 3 1V10a1.5 1.5 0 0 1-1.5 1.5C5 11.5.5 7 .5 2.5A1.5 1.5 0 0 1 2 1z" fill="#fff"/></svg>
        <svg viewBox="0 0 12 12"><rect x="0.5" y="2.5" width="11" height="7" fill="none" stroke="#fff"/><path d="M.5 2.5 6 7l5.5-4.5" fill="none" stroke="#fff"/></svg>
        <svg viewBox="0 0 12 12"><circle cx="6" cy="6" r="5.3" fill="none" stroke="#fff"/><ellipse cx="6" cy="6" rx="2.3" ry="5.3" fill="none" stroke="#fff"/><path d="M.7 6h10.6" stroke="#fff"/></svg>
      </div>
      <ul class="contact__list">
        <li>301-647-9183</li>
        <li>301-836-7100</li>
        <li>dora@dorabeckhomes.com</li>
        <li>dorabeckhomes.com</li>
      </ul>
    </div>
  </div>
  <div class="stamp-box"></div>
  <div class="address-line" style="top:240px"></div>
  <div class="address-line" style="top:270px"></div>
  <div class="address-line" style="top:300px"></div>
  <div class="address-line" style="top:330px"></div>
</section>

<section class="card card--message" aria-label="Message side">
  <div class="tile tile--beach">
    <div class="tile__image" role="img" aria-label="Tropical beach with palm tree and sea"></div>
    <p class="tile__caption"><span>Wish you</span><span>were there</span><span>year round?</span></p>
  </div>
  <div class="tile tile--condo">
    <div class="tile__image" role="img" aria-label="Upscale city condo tower"></div>
    <p class="tile__caption"><span>Ready for</span><span>one-level</span><span class="big">living?</span></p>
  </div>
  <div class="tile tile--tax">
    <div class="tile__image" role="img" aria-label="Calculator and pen on a property tax bill"></div>
    <p class="tile__caption"><span>Time to</span><span>down-size</span><span>expenses?</span></p>
  </div>
  <div class="tile tile--snow">
    <div class="tile__image" role="img" aria-label="Snow-covered cars and a person shoveling snow"></div>
    <p class="tile__caption"><span>Done with</span><span>winters?</span></p>
  </div>
  <p class="cta-band">If you answered "YES", then we need to talk!</p>
</section>

</body>
</html>
```